website re-design for: kestra+grove, complete vision care

we are a growing, cutting edge eye clinic with two locations in the palouse area of washington state, in the usa. we offer complete vision care, from spectacles and contacts to ocular disease management and treatment.

our current website was designed as a freebie, and was always meant to be a placeholder. we have reached a point where we would like our website to have a more stand-apart look and feel, while maintaining an intuitive user experience.

Target Market(s)

because our two clinics serve vastly different demographics, the website will have to speak to both. one clinic is located in a college town (majority of patients are 18-50 years+), while the other serves an older adult population (majority of patients 30-75 yrs+).

Industry/Entity Type

Health And Wellness

Logo Text

kestra+grove (including a logo lock-up version w/ "complete vision care")

Coding

Coded - Design and coding required

Number of Pages Required

5+ page

Font styles to use
Sans Serif
Other font styles liked:
• Verdana, and complementary fonts

Colors
606060
ffffff
33b8a4
86cfc6

Requirements
Must have
• - Pertinent contact information w/ Google maps
• - Clinic phone numbers at top of each page
• - An appointment request form
• - Page for Blog
• - Integrate with overall brand look and feel (e.g. Verdana font (we are open to complementary fonts), all lower case, except for prose,
• - Mobile friendly design
• - Code to maximize Search Engine Optimization (SEO)
Nice to have
• a design that speaks to the true nature of our business as an eye clinic, but feels different than typical eye care websites
Should not have
• this probably goes without saying, but the website should not have any political slant or otherwise bias

```html
<!DOCTYPE html>
<html lang="en">
<head>
<meta charset="utf-8">
<title>kestra+grove — complete vision care</title>
<link href="https://fonts.googleapis.com/css2?family=Lato:wght@300;400;700;900&display=swap" rel="stylesheet">
<style>
:root{
  --ink:#1c1c1c;
  --grey:#606060;
  --white:#ffffff;
  --teal:#33b8a4;
  --teal-deep:#1f9e88;
  --teal-soft:#86cfc6;
  --mint:#e8f5f2;
  --footer:#2a2a2a;
  --alert:#c64b4b;
}
*{margin:0;padding:0;box-sizing:border-box}
html,body{width:683px;height:1200px;overflow:hidden}
body{font-family:'Lato',Verdana,sans-serif;background:var(--mint);color:var(--ink);position:relative}
.hero{position:absolute;left:0;top:0;width:683px;height:375px;
  background:radial-gradient(ellipse at 50% 35%,#4a4a4a 0%,#333 45%,#262626 100%)}
.brand{position:absolute;left:27px;top:8px;display:flex;align-items:flex-start;gap:8px;color:var(--white)}
.brand-mark{width:40px;height:40px;background:var(--teal);margin-top:2px}
.brand-name{font-size:20px;line-height:23px;font-weight:400}
.brand-tag{position:absolute;left:75px;top:51px;font-size:10px;color:var(--white)}
.phones-top{position:absolute;right:86px;top:20px;color:var(--white);font-size:12.5px;line-height:19px;text-align:right}
.phones-top b{font-weight:700}
.menu-btn{position:absolute;left:633px;top:27px;width:25px;height:21px;display:flex;flex-direction:column;justify-content:space-between}
.menu-btn span{display:block;height:4px;background:var(--white)}
.hero-title{position:absolute;left:0;width:683px;top:150px;text-align:center;color:var(--white);
  font-size:37px;font-weight:400;font-variant:small-caps;letter-spacing:.5px}
.btn{position:absolute;left:258px;top:230px;width:167px;height:32px;background:var(--teal);color:var(--white);
  font-size:11.5px;display:flex;align-items:center;justify-content:center;border-radius:2px;
  box-shadow:3px 4px 6px rgba(0,0,0,.45)}
.intro{position:absolute;left:80px;top:338px;width:523px;height:224px;border-radius:4px;
  background:linear-gradient(160deg,#2fb39e 0%,#28a894 55%,#34b5a1 100%);
  color:var(--white);font-size:13.4px;line-height:20px;text-align:center;padding:50px 50px 0;letter-spacing:.6px}
.section-title{position:absolute;left:0;width:683px;top:604px;text-align:center;font-size:23px;font-weight:900;
  color:#173c36;text-shadow:2px 2px 0 var(--teal)}
.clinic{position:absolute;top:672px;width:202px;font-size:9.4px}
.clinic.pullman{left:80px}
.clinic.clarkston{left:401px}
.clinic h3{text-align:center;font-size:12px;font-weight:700;margin-bottom:5px}
.hours{display:grid;grid-template-columns:1fr auto;row-gap:1px;line-height:12.5px}
.hours dd{color:var(--grey)}
.map{position:absolute;left:0;top:63px;width:202px;height:113px;border:2px solid #ddd;
  background:linear-gradient(135deg,#efe8d8 0%,#e2e6cf 40%,#f1ead6 70%,#e6e4dc 100%);box-shadow:1px 2px 4px rgba(0,0,0,.35)}
.address{position:absolute;top:194px;left:0;width:202px;text-align:center;font-size:11px;line-height:13px;font-weight:300;color:#444}
.contact{position:absolute;top:251px;left:0;width:202px;font-size:9.5px}
.contact-row{display:flex;align-items:center;height:18px}
.contact-row .label{font-size:11px;display:flex;align-items:center;gap:5px;color:var(--ink)}
.contact-row .value{margin-left:auto;color:var(--grey)}
.notice{position:absolute;top:296px;left:0;width:202px;text-align:center;color:var(--alert);font-size:9.5px;line-height:12px;font-weight:300}
.notice svg{vertical-align:-1px;margin-right:4px}
.footer{position:absolute;left:0;top:1030px;width:683px;height:170px;background:var(--footer);color:var(--white)}
.footer .brand{top:18px}
.footer-phones{position:absolute;left:27px;top:75px;font-size:9.5px;line-height:15.5px;display:grid;grid-template-columns:63px auto}
.footer-legal{position:absolute;left:27px;top:112px;font-size:8.5px;color:#ddd}
.footer-about{position:absolute;left:211px;top:22px;width:262px;text-align:center}
.footer-about h4{font-size:9.5px;font-weight:700;line-height:14px;margin:0 auto 11px;width:210px}
.footer-about p{font-size:8.6px;line-height:14px;color:#ddd;font-weight:400}
.footer-about u{color:#eee}
.footer-nav{position:absolute;right:27px;top:23px;text-align:right;list-style:none;font-size:11.5px;line-height:20px;font-weight:300}
.copyright{position:absolute;left:0;top:153px;width:683px;text-align:center;font-size:6.5px;color:#bbb}
</style>
</head>
<body>

<header class="hero" role="img" aria-label="Photo of a hand holding a pair of glasses with droplets on the lenses">
</header>
<div class="brand">
  <div class="brand-mark"></div>
  <div class="brand-name">kestra+<br>grove</div>
</div>
<div class="brand-tag">complete vision care</div>
<div class="phones-top"><b>Pullman</b> 509-555-0142<br><b>Clarkston</b> 509-555-0187</div>
<div class="menu-btn" aria-label="Menu"><span></span><span></span><span></span></div>
<h1 class="hero-title">An Eye on the Future</h1>
<a class="btn">Request an Appointment</a>

<section class="intro" role="img" aria-label="Soft teal background with a faint photo of eyeglasses">
  Eyes are important indicators of overall health, and comprehensive eye care goes beyond a prescription for glasses or contact lenses. At kestra+grove, we take the time to get to know you, your eye care history, and your vision needs. Our optometrist provides the expert care, advice, options, and follow up you need whether you are a new patient or an existing one.
</section>

<h2 class="section-title">Come In And See Us</h2>

<div class="clinic pullman">
  <h3>Pullman</h3>
  <dl class="hours"><dt>Tuesday</dt><dd>9:00 AM - 5:00 PM</dd><dt>Saturday</dt><dd>9:00 AM - 5:00 PM</dd></dl>
  <div class="map" role="img" aria-label="Map of the Pullman clinic location"></div>
  <p class="address">Orchard Vision Center<br>1420 SE Orchard Lane<br>Pullman, WA 99163</p>
  <div class="contact">
    <div class="contact-row"><span class="label"><svg width="11" height="11" viewBox="0 0 24 24"><path fill="#111" d="M6.6 10.8a15 15 0 0 0 6.6 6.6l2.2-2.2c.3-.3.7-.4 1-.2 1.1.4 2.3.6 3.6.6.6 0 1 .4 1 1V20c0 .6-.4 1-1 1A17 17 0 0 1 3 4c0-.6.4-1 1-1h3.5c.6 0 1 .4 1 1 0 1.2.2 2.4.6 3.6.1.3 0 .7-.2 1z"/></svg>Phone:</span><span class="value">509-555-0142</span></div>
    <div class="contact-row"><span class="label"><svg width="13" height="10" viewBox="0 0 26 20"><rect width="26" height="20" rx="2" fill="#111"/><path d="M1 2l12 9 12-9" stroke="#e8f5f2" stroke-width="2" fill="none"/></svg>E-mail:</span><span class="value">contact@kestragrovewa.com</span></div>
  </div>
  <p class="notice"><svg width="10" height="10" viewBox="0 0 20 20"><circle cx="10" cy="10" r="10" fill="#c01f1f"/><rect x="9" y="4" width="2" height="8" fill="#fff"/><rect x="9" y="14" width="2" height="2" fill="#fff"/></svg>Do not send personal health information<br>by email</p>
</div>

<div class="clinic clarkston">
  <h3>Clarkston</h3>
  <dl class="hours"><dt>Tuesday</dt><dd>9:00 AM - 5:00 PM</dd><dt>Saturday</dt><dd>9:00 AM - 5:00 PM</dd><dt>Friday</dt><dd>9:00 AM - 5:00 PM</dd></dl>
  <div class="map" role="img" aria-label="Map of the Clarkston clinic location"></div>
  <p class="address">Orchard Vision Center<br>218 Bridge Street<br>Clarkston, WA 99403</p>
  <div class="contact">
    <div class="contact-row"><span class="label"><svg width="11" height="11" viewBox="0 0 24 24"><path fill="#111" d="M6.6 10.8a15 15 0 0 0 6.6 6.6l2.2-2.2c.3-.3.7-.4 1-.2 1.1.4 2.3.6 3.6.6.6 0 1 .4 1 1V20c0 .6-.4 1-1 1A17 17 0 0 1 3 4c0-.6.4-1 1-1h3.5c.6 0 1 .4 1 1 0 1.2.2 2.4.6 3.6.1.3 0 .7-.2 1z"/></svg>Phone:</span><span class="value">509-555-0187</span></div>
    <div class="contact-row"><span class="label"><svg width="13" height="10" viewBox="0 0 26 20"><rect width="26" height="20" rx="2" fill="#111"/><path d="M1 2l12 9 12-9" stroke="#e8f5f2" stroke-width="2" fill="none"/></svg>E-mail:</span><span class="value">contact@kestragrovewa.com</span></div>
  </div>
  <p class="notice"><svg width="10" height="10" viewBox="0 0 20 20"><circle cx="10" cy="10" r="10" fill="#c01f1f"/><rect x="9" y="4" width="2" height="8" fill="#fff"/><rect x="9" y="14" width="2" height="2" fill="#fff"/></svg>Do not send personal health information<br>by email</p>
</div>

<footer class="footer">
  <div class="brand">
    <div class="brand-mark"></div>
    <div class="brand-name">kestra+<br>grove</div>
  </div>
  <div class="footer-phones"><span>Pullman</span><span>509-555-0142</span><span>Clarkston</span><span>509-555-0187</span></div>
  <div class="footer-legal">Disclaimer | Privacy Policy</div>
  <div class="footer-about">
    <h4>Great Eyewear and Eye Care in Pullman and Clarkston, Washington</h4>
    <p>From our offices in Pullman and Clarkston, kestra+grove serves southeastern Washington. – <u>schedule an appointment today</u>. If you have a moment, please give us <u>your feedback</u> about our site and your experiences with our Practice.</p>
  </div>
  <ul class="footer-nav">
    <li>Hours &amp; Location</li>
    <li>Our Eye Doctor</li>
    <li>Our Eye Care Clinic</li>
    <li>Eye Care Services</li>
    <li>Insurance</li>
  </ul>
  <p class="copyright">Copyright © kestra+grove | Powered by ClearSitePro.net | Email Accessibility | Website Accessibility Policy | Login</p>
</footer>

</body>
</html>
```